Logistics Website Design

See website https://tvarfreightglobal.com for theme and color details. Need the site to be re-done and reflect some of the designs shown in this list here: https://pinvora.com/tags/logistics-company-website

Target Market(s)

Logistics & Transportation

Industry/Entity Type

Logistics and Supply Chain

Coding

Coded - Design and coding required

Number of Pages Required

5+ page

Requirements
Must have
• Colors must match theme of logo. Looking for a sleek, interactive design.

```html
<!DOCTYPE html>
<html lang="en">
<head>
<meta charset="utf-8">
<title>Tvar Freight Global — Logistics</title>
<link href="https://fonts.googleapis.com/css2?family=Poppins:wght@400;500;600;700&family=Racing+Sans+One&display=swap" rel="stylesheet">
<style>
:root{
  --bg:#120604;
  --bg-band:#2a130d;
  --bg-footer:#140704;
  --orange:#ea6a3e;
  --orange-dark:#b9461f;
  --pink:#f2a88f;
  --pink-light:#f9d6cb;
  --ink:#1a0a05;
  --text:#f4e6df;
  --muted:#c9b3aa;
  --field:#4a2419;
}
*{margin:0;padding:0;box-sizing:border-box}
html,body{width:1200px;height:3062px;overflow:hidden}
body{position:relative;background:var(--bg);font-family:"Poppins",sans-serif;color:var(--text)}
.abs{position:absolute}
.display{font-family:"Racing Sans One","Poppins",sans-serif;font-style:italic;letter-spacing:1px;text-transform:uppercase;line-height:1}
.btn{position:absolute;display:flex;align-items:center;justify-content:center;background:var(--orange);color:var(--ink);font-weight:700;font-size:11px;text-transform:uppercase;border-bottom:4px solid var(--orange-dark);border-radius:3px;letter-spacing:.3px}
.photo{position:absolute}

/* header */
.brand{position:absolute;left:154px;top:14px;display:flex;align-items:center;gap:10px}
.brand-dot{width:44px;height:44px;border-radius:50%;background:var(--orange)}
.brand-name{font-weight:700;font-size:15px;line-height:1.15;color:var(--orange);text-transform:uppercase;width:80px}
.nav{position:absolute;top:28px;left:530px;display:flex;gap:0;font-size:11.5px;font-weight:600;text-transform:uppercase}
.nav a{position:absolute;white-space:nowrap;color:var(--text);text-decoration:none}
/* hero */
.hero-photo{left:0;top:0;width:1200px;height:737px;background:radial-gradient(ellipse at 70% 35%,#7a4a35 0%,#3c2219 35%,#1a0b07 70%,var(--bg) 100%)}
.hero-truck{left:540px;top:214px;width:660px;height:346px;background:linear-gradient(135deg,#c25a2c 0%,#8a3b1c 40%,#6b6d74 60%,#3a3a40 100%);border-radius:8px;opacity:.85}
.slides{left:48px;top:374px;font-size:13px;color:var(--muted);text-align:right;width:50px}
.slides .cur{color:var(--orange);font-size:22px;line-height:1.2}
.hero-kicker{left:148px;top:293px;font-size:36px;color:var(--orange)}
.hero-big{left:148px;top:336px;font-size:66px;color:var(--orange)}
.hero-sub-title{left:148px;top:406px;font-size:36px;color:var(--orange)}
.hero-text{left:150px;top:447px;font-size:13.5px}
/* about */
.section-label{color:var(--orange)}
.about-p{left:624px;top:1036px;width:414px;font-size:13.2px;line-height:21.2px}
</style>
</head>
<body>

<header>
  <div class="brand"><span class="brand-dot"></span><span class="brand-name">Tvar Freight Global</span></div>
  <nav class="nav" aria-label="Main">
    <svg class="abs" style="left:2px;top:0" width="12" height="12" viewBox="0 0 12 12"><path d="M6 1 1 6h1.5v5h3V8h1v3h3V6H11z" fill="var(--orange)"/></svg>
    <a style="left:37px">Services</a>
    <a style="left:114px">Industries</a>
    <a style="left:218px">Request a Quote</a>
    <a style="left:320px">About Us</a>
  </nav>
  <div class="btn" style="left:947px;top:19px;width:101px;height:32px">Contact Us</div>
</header>

<section class="hero">
  <div class="photo hero-photo" role="img" aria-label="Dusky desert highway background"></div>
  <div class="photo hero-truck" role="img" aria-label="Orange semi truck with grey trailer speeding on a highway"></div>
  <div class="abs slides"><div>01</div><div class="cur">— 02</div><div>03</div></div>
  <div class="abs display hero-kicker">Delivering</div>
  <div class="abs display hero-big">Strength</div>
  <div class="abs display hero-sub-title">In Every Mile</div>
  <p class="abs hero-text">Secure and reliable transportation for all your cargo needs.</p>
  <div class="btn" style="left:150px;top:479px;width:133px;height:31px">Request a Quote</div>
  <svg class="abs" style="left:592px;top:657px" width="16" height="24" viewBox="0 0 16 24"><rect x="1" y="1" width="14" height="22" rx="7" fill="none" stroke="var(--muted)" stroke-width="1.5"/><line x1="8" y1="5" x2="8" y2="10" stroke="var(--muted)" stroke-width="1.5"/></svg>
</section>

<section class="about">
  <div class="photo" style="left:131px;top:808px;width:86px;height:172px;background:#6a2d1c;opacity:.5" role="img" aria-label="Dotted accent"></div>
  <div class="photo" style="left:170px;top:843px;width:327px;height:382px;background:linear-gradient(160deg,#b8b5b0 0%,#8a8680 35%,#e0662e 60%,#8a3a1d 100%)" role="img" aria-label="Orange truck cab beside city buildings"></div>
  <div class="photo" style="left:347px;top:1111px;width:198px;height:180px;background:linear-gradient(180deg,#b59a7e 0%,#8b7a62 55%,#6c6258 100%)" role="img" aria-label="Flatbed truck hauling cargo on a desert road"></div>
  <div class="abs" style="left:497px;top:871px;width:477px;height:1px;background:#4a2a20"></div>
  <div class="abs" style="left:556px;top:1271px;width:157px;height:1px;background:#4a2a20"></div>
  <div class="abs display section-label" style="left:627px;top:933px;font-size:18px">About Us</div>
  <div class="abs display section-label" style="left:627px;top:956px;font-size:35px;line-height:39px">Keeping Your Supply<br>Chain Moving</div>
  <p class="abs about-p">We deliver a comprehensive range of open-deck and specialized transportation services—including flatbed, step deck, heavy haul, and over-dimensional freight solutions. Backed by years of experience, a trusted nationwide carrier network, and a strong safety-first culture, we provide reliable, adaptable logistics support built around the unique requirements of every load.</p>
  <div class="btn" style="left:624px;top:1182px;width:102px;height:31px">Read More</div>
</section>

<section class="services">
  <div class="abs display" style="left:0;width:1200px;text-align:center;top:1372px;font-size:36px;color:var(--orange)">Our Services</div>
  <div class="abs" style="left:0;top:1592px;width:1200px;height:434px;background:var(--pink)"></div>
  <div class="photo" style="left:867px;top:1746px;width:333px;height:280px;background:linear-gradient(90deg,rgba(242,168,143,0) 0%,#9a4a2c 45%,#3c2a28 75%,#c0633a 100%)" role="img" aria-label="Dark semi truck on an orange-lit highway"></div>

  <!-- cards -->
  <style>
    .card{position:absolute;top:1441px;width:217px;height:309px}
    .card-img{position:absolute;left:6px;top:0;width:205px;height:151px}
    .card-body{position:absolute;left:0;top:151px;width:217px;height:158px;background:var(--pink-light);border:2px solid var(--ink);border-top:none}
    .card-icon{position:absolute;left:20px;top:130px;width:41px;height:41px;background:var(--ink);display:flex;align-items:center;justify-content:center}
    .card-title{position:absolute;left:20px;top:184px;font-weight:700;font-size:13px;line-height:16px;color:var(--ink);text-transform:uppercase}
    .card-desc{position:absolute;left:20px;top:219px;width:182px;font-size:10.8px;line-height:15px;color:var(--ink)}
  </style>
  <div class="card" style="left:150px">
    <div class="photo card-img" style="background:linear-gradient(180deg,#c8c8c6 0%,#8a3a3a 50%,#4a4a4a 100%)" role="img" aria-label="Flatbed trailer wheels"></div>
    <div class="card-body"></div>
    <div class="card-icon"><svg width="24" height="16" viewBox="0 0 24 16"><path d="M1 11h14V4h5l3 4v3h-1M3 13h18" fill="none" stroke="var(--pink)" stroke-width="1.5"/><circle cx="6" cy="13" r="2" fill="var(--pink)"/><circle cx="18" cy="13" r="2" fill="var(--pink)"/></svg></div>
    <div class="card-title">Flatbed<br>Transportation</div>
    <div class="card-desc">From routine shipments to oversized and heavy-haul loads…</div>
    <div class="btn" style="left:21px;top:260px;width:102px;height:30px">Read More</div>
  </div>
  <div class="card" style="left:379px">
    <div class="photo card-img" style="background:linear-gradient(180deg,#8a9bb0 0%,#c63a2a 55%,#b8b0a8 100%)" role="img" aria-label="Red step deck trailer in a yard"></div>
    <div class="card-body"></div>
    <div class="card-icon"><svg width="24" height="16" viewBox="0 0 24 16"><path d="M1 11h14V4h5l3 4v3h-1M3 13h18" fill="none" stroke="var(--pink)" stroke-width="1.5"/><circle cx="6" cy="13" r="2" fill="var(--pink)"/><circle cx="18" cy="13" r="2" fill="var(--pink)"/></svg></div>
    <div class="card-title">Step Deck<br>Transportation</div>
    <div class="card-desc">Our step deck trucking services support tall, heavy, and speciali…</div>
    <div class="btn" style="left:21px;top:260px;width:102px;height:30px">Read More</div>
  </div>
  <div class="card" style="left:607px">
    <div class="photo card-img" style="background:linear-gradient(180deg,#8a8a95 0%,#b86a50 45%,#2a2628 100%)" role="img" aria-label="Dry van trailers at sunset"></div>
    <div class="card-body"></div>
    <div class="card-icon"><svg width="24" height="16" viewBox="0 0 24 16"><path d="M1 11h14V4h5l3 4v3h-1M3 13h18" fill="none" stroke="var(--pink)" stroke-width="1.5"/><circle cx="6" cy="13" r="2" fill="var(--pink)"/><circle cx="18" cy="13" r="2" fill="var(--pink)"/></svg></div>
    <div class="card-title">Dry Van<br>Transportation</div>
    <div class="card-desc">From consumer goods to industrial materials, our dry van services…</div>
    <div class="btn" style="left:21px;top:260px;width:102px;height:30px">Read More</div>
  </div>
  <div class="card" style="left:835px">
    <div class="photo card-img" style="background:linear-gradient(180deg,#6a7a6a 0%,#d0a830 45%,#b83a30 70%,#8a8a8a 100%)" role="img" aria-label="Heavy haul truck carrying an excavator"></div>
    <div class="card-body"></div>
    <div class="card-icon"><svg width="24" height="16" viewBox="0 0 24 16"><path d="M1 11h14V4h5l3 4v3h-1M3 13h18" fill="none" stroke="var(--pink)" stroke-width="1.5"/><circle cx="6" cy="13" r="2" fill="var(--pink)"/><circle cx="18" cy="13" r="2" fill="var(--pink)"/></svg></div>
    <div class="card-title">Heavy Haul<br>Transportation</div>
    <div class="card-desc">We provide heavy haul trucking solutions for oversized, overweig…</div>
    <div class="btn" style="left:21px;top:260px;width:102px;height:30px">Read More</div>
  </div>

  <div class="abs display" style="left:0;width:1200px;text-align:center;top:1832px;font-size:36px;color:var(--ink)">Request a Quote</div>
  <p class="abs" style="left:0;width:1200px;text-align:center;top:1876px;font-size:13.5px;color:var(--ink)">Tell us what you're moving and we'll respond with pricing, options, and timelines.</p>
  <div class="btn" style="left:533px;top:1910px;width:134px;height:30px">Get Started</div>
</section>

<section class="industries">
  <style>
    .ind{position:absolute;top:2236px;width:171px;height:170px;border:2px solid var(--orange);display:flex;flex-direction:column;align-items:center}
    .ind svg{position:absolute;top:30px}
    .ind-label{position:absolute;top:110px;width:100%;text-align:center;font-weight:700;font-size:13.5px;line-height:16px;color:var(--orange);text-transform:uppercase}
  </style>
  <div class="abs display" style="left:0;width:1200px;text-align:center;top:2120px;font-size:36px;color:var(--orange)">Industries We Serve</div>
  <p class="abs" style="left:0;width:1200px;text-align:center;top:2168px;font-size:13px;line-height:21px;color:var(--orange)">Providing tailored logistics solutions for every industry, ensuring<br>your cargo moves safely and on time.</p>

  <div class="ind" style="left:150px">
    <svg width="60" height="60" viewBox="0 0 60 60" fill="none" stroke="var(--pink)" stroke-width="2"><rect x="6" y="30" width="36" height="24"/><rect x="42" y="38" width="12" height="16"/><path d="M14 30V18h8v12M30 30V8h8v22"/></svg>
    <div class="ind-label">Food &amp;<br>Beverage</div>
  </div>
  <div class="ind" style="left:331px">
    <svg width="60" height="60" viewBox="0 0 60 60" fill="none" stroke="var(--pink)" stroke-width="2"><path d="M14 8h32l4 10H10z"/><rect x="14" y="18" width="32" height="38"/><path d="M22 32h16l-2 10H24zM20 28h2"/><circle cx="26" cy="46" r="2"/><circle cx="34" cy="46" r="2"/></svg>
    <div class="ind-label">E-Commerce<br>&amp; Retail</div>
  </div>
  <div class="ind" style="left:513px">
    <svg width="66" height="60" viewBox="0 0 66 60" fill="none" stroke="var(--pink)" stroke-width="2"><circle cx="26" cy="22" r="11"/><circle cx="26" cy="22" r="5"/><path d="M26 5v6M26 33v6M9 22h6M37 22h6M14 10l4 4M34 30l4 4M14 34l4-4M34 14l4-4"/><rect x="44" y="30" width="12" height="12"/><rect x="4" y="44" width="58" height="10" rx="5"/><circle cx="14" cy="49" r="2"/><circle cx="26" cy="49" r="2"/><circle cx="38" cy="49" r="2"/><circle cx="50" cy="49" r="2"/></svg>
    <div class="ind-label" style="top:120px">Manufacturing</div>
  </div>
  <div class="ind" style="left:696px">
    <svg width="60" height="60" viewBox="0 0 60 60" fill="none" stroke="var(--pink)" stroke-width="2"><rect x="6" y="6" width="20" height="16" rx="2"/><path d="M16 10v8M12 14h8"/><circle cx="44" cy="12" r="6"/><path d="M10 28h8v16H10zM30 30v10l-8 12h24l-8-12V30M28 30h12"/><path d="M8 54h48"/></svg>
    <div class="ind-label">Pharma &amp;<br>Healthcare</div>
  </div>
  <div class="ind" style="left:877px">
    <svg width="66" height="60" viewBox="0 0 66 60" fill="none" stroke="var(--pink)" stroke-width="2"><path d="M4 12h36v30H4zM40 22h12l8 10v10H40"/><circle cx="14" cy="46" r="5"/><circle cx="50" cy="46" r="5"/><path d="M22 18l8 3v6c0 5-4 8-8 9-4-1-8-4-8-9v-6z"/></svg>
    <div class="ind-label">Government<br>Secured Freight</div>
  </div>
</section>

<section class="signup">
  <div class="abs" style="left:0;top:2500px;width:1200px;height:319px;background:var(--bg-band)"></div>
  <div class="abs display" style="left:0;width:1200px;text-align:center;top:2594px;font-size:33px;line-height:36px;color:var(--orange)">Signup to receive our offer,<br>and stay upto date</div>
  <div class="abs" style="left:246px;top:2686px;width:270px;height:47px;background:var(--field);border-radius:4px;font-size:11px;color:var(--muted);padding:16px 16px">Your Name</div>
  <div class="abs" style="left:527px;top:2686px;width:270px;height:47px;background:var(--field);border-radius:4px;font-size:11px;color:var(--muted);padding:16px 16px">Email Address</div>
  <div class="abs" style="left:809px;top:2686px;width:144px;height:47px;background:var(--orange);border-radius:4px;display:flex;align-items:center;justify-content:center;gap:8px;font-family:'Racing Sans One',sans-serif;font-style:italic;font-size:12px;color:var(--ink);text-transform:uppercase">Submit
    <svg width="14" height="14" viewBox="0 0 14 14"><path d="M13 1 1 6l5 2 2 5z" fill="var(--ink)"/></svg></div>
</section>

<footer>
  <div class="abs" style="left:0;top:2819px;width:1200px;height:243px;background:var(--bg-footer)"></div>
  <div class="abs" style="left:211px;top:2910px;display:flex;align-items:center;gap:12px">
    <span style="width:56px;height:56px;border-radius:50%;background:var(--orange)"></span>
    <span style="font-weight:700;font-size:19px;line-height:1.15;color:var(--orange);text-transform:uppercase;width:100px">Tvar Freight Global</span>
  </div>
  <div class="abs" style="top:2897px;left:0;width:1200px;font-size:11px;font-weight:500;text-transform:uppercase">
    <span class="abs" style="left:543px">Services</span>
    <span class="abs" style="left:619px">Industries</span>
    <span class="abs" style="left:707px">Request a Quote</span>
    <span class="abs" style="left:830px">About Us</span>
    <span class="abs" style="left:911px">Contact Us</span>
  </div>
  <p class="abs" style="left:600px;width:380px;text-align:right;top:2920px;font-size:10.5px">© 2026. An independent agent of Brell Haskin LLC.</p>
  <div class="abs" style="left:866px;top:2946px;width:36px;height:36px;border-radius:50%;background:#3a1d14;display:flex;align-items:center;justify-content:center">
    <svg width="16" height="16" viewBox="0 0 16 16" fill="none" stroke="var(--pink-light)" stroke-width="1.4"><circle cx="8" cy="8" r="6.5"/><path d="M1.5 8h13M8 1.5c-3 3.5-3 9.5 0 13M8 1.5c3 3.5 3 9.5 0 13"/></svg></div>
  <div class="abs" style="left:907px;top:2946px;width:36px;height:36px;border-radius:50%;background:#3a1d14;display:flex;align-items:center;justify-content:center">
    <svg width="16" height="12" viewBox="0 0 16 12"><rect width="16" height="12" rx="1.5" fill="var(--pink-light)"/><path d="M1 1.5 8 7l7-5.5" fill="none" stroke="#3a1d14" stroke-width="1.4"/></svg></div>
  <div class="abs" style="left:948px;top:2946px;width:36px;height:36px;border-radius:50%;background:#3a1d14;display:flex;align-items:center;justify-content:center">
    <svg width="15" height="15" viewBox="0 0 16 16"><path d="M3 1h3l1.5 4-2 1.3a9 9 0 0 0 4.2 4.2L11 8.5l4 1.5v3a2 2 0 0 1-2 2C6.5 15 1 9.5 1 3a2 2 0 0 1 2-2z" fill="var(--pink-light)"/></svg></div>
  <div class="abs" style="left:1112px;top:2941px;width:28px;height:28px;border-radius:50%;background:var(--pink);display:flex;align-items:center;justify-content:center">
    <svg width="10" height="8" viewBox="0 0 10 8"><path d="M1 6 5 2l4 4" fill="none" stroke="var(--ink)" stroke-width="1.6"/></svg></div>
</footer>

</body>
</html>
```